Web Design Project - Shipping Industry

Goals and Objectives
The objective of the new website is to create a more modern look and feel. The site will also allow for a more effective means of communicating with members while providing the public with information and developments in the local, regional and international shipping industry.
Scope
The website will highlight the history of the organisation inclusive of text and photographs. It will take visitors through the years from beginning to present. Information on the history of the shipping industry will also be included.
It will feature current articles on the organisation, its members and stakeholders in the shipping industry. Member information as well as pertinent details regarding the organisation’s subsidiaries will be documented for the website.
Information as it relates to shipping statistics, case studies, laws and regulations, international treaties and trade documents, shipping terms, careers in shipping, job opportunities, training opportunities, information for shippers including port listing and trade lanes will be main features of the content for the website.
The Association’s community involvement, industry calendar events and related links relevant industry members will also be featured.
Target Market
• The General Public;
• Members of the organization;
• Shipping Industry Stakeholders (local, regional and international);
• Tertiary students conducting research.
• Potential employees
• Potential Business Partners
Best Practice Bench Marketing
The following websites are being looked at:
• Velloric Docks - http://www.vellori-docks.example/ (preferred look)
• Corvane Maritime Association - http://www.cmx-assoc.example/ (like image transition on main page)
• Trovald - http://www.trovald.example (professional look)
• KBU - http://www.quaylinx.example (preferred color: blue in logo)
• Wuzo - http://www.wuzo.example/electronics/tv-video-audio/ (preferred look for links page: image + short text below + visit site link)
Expected Result
• 3 - 5 pages which must include: [1] main page [2] standard page [3] links page
Target Market(s)
The General Public; Members of the organization; Shipping Industry Stakeholders (local, regional and international); Tertiary students conductin
Industry/Entity Type
Shipping
Look and feel

```html
<!DOCTYPE html>
<html lang="en">
<head>
<meta charset="utf-8">
<title>The Shipping Association of Kelbury</title>
<link href="https://fonts.googleapis.com/css2?family=Arimo:wght@400;700&family=Roboto+Condensed:wght@400;700&display=swap" rel="stylesheet">
<style>
:root{
  --ink:#222;
  --body:#444;
  --blue:#1f5fb8;
  --blue-dark:#0f4a9e;
  --lime:#c3cc10;
  --lime-dark:#a8b00a;
  --rule:#b5b5b5;
  --footer:#111;
  --panel:#e8f0f8;
}
*{box-sizing:border-box;margin:0;padding:0}
html,body{width:830px;height:1200px;overflow:hidden;background:#fff}
body{position:relative;font-family:"Arimo",Arial,sans-serif;color:var(--body);font-size:10px}
.abs{position:absolute}
.topline{left:0;top:0;width:830px;height:7px;background:#111}
.brand{left:9px;top:17px;display:flex;align-items:flex-start;gap:8px;z-index:2}
.brand-mark{width:52px;height:52px;border-radius:50%;background:var(--blue)}
.brand-name{font-size:19px;color:var(--blue-dark);font-weight:400;margin-top:5px;white-space:nowrap}
.contact{left:571px;top:7px;width:250px;height:29px;background:var(--blue);border-radius:0 0 4px 4px;color:#fff;font-size:12.5px;display:flex;align-items:center;justify-content:space-between;padding:0 12px;white-space:nowrap}
.contact span{display:flex;align-items:center;gap:5px}
.nav{left:114px;top:51px;width:707px;height:39px;background:linear-gradient(#2a6cc4,#1553a8);display:flex}
.nav a{color:#fff;text-decoration:none;font-size:13.5px;padding:0 14px;display:flex;align-items:center;border-right:1px solid #3c78c8}
.nav a.active{background:linear-gradient(#d8de2a,#b5bc08);color:#111;padding:0 15px}
.hero{left:9px;top:102px;width:812px;height:380px;border-radius:4px;background:linear-gradient(#6f9cc6 0%,#b8d0e2 55%,#7a9aa8 72%,#3f6370 100%)}
.dots{left:385px;top:462px;display:flex;gap:5px}
.dots i{width:10px;height:10px;border-radius:50%;background:#222}
.dots i:first-child{background:#fff}
.login{left:592px;top:115px;width:216px;height:174px}
.tabs{display:flex;gap:2px}
.tabs span{font-size:11.5px;font-weight:700;padding:6px 8px;border-radius:3px 3px 0 0}
.tab-on{background:var(--panel);color:var(--blue-dark)}
.tab-off{background:var(--blue);color:#fff}
.login-body{background:var(--panel);padding:10px 12px;height:148px;border-radius:0 3px 3px 3px}
.login-body label{display:block;font-size:11px;color:#333;margin-bottom:5px}
.field{height:22px;background:#fff;border:1px solid #9cc1e6;border-radius:2px;margin-bottom:10px}
.login-row{display:flex;align-items:center;gap:8px}
.btn-blue{background:var(--blue);color:#fff;font-size:11.5px;padding:4px 8px;border-radius:3px}
.forgot{font-size:9.5px;color:var(--blue)}
h2.section{font-family:"Roboto Condensed",Arial,sans-serif;font-weight:700;font-size:15px;color:#333;padding-bottom:6px;border-bottom:1px dashed var(--rule)}
.photo{border:1px solid #bbb}
.welcome-h{left:9px;top:497px;width:633px}
.welcome-img{left:9px;top:529px;width:143px;height:133px;background:linear-gradient(135deg,#c7d2da,#a27a60 55%,#e6e6e6)}
.welcome-text{left:162px;top:527px;width:480px;line-height:17.4px;font-size:9.4px;letter-spacing:.2px;height:106px;overflow:hidden}
.btn-lime{background:linear-gradient(#d3da1e,#b3ba07);color:#222;font-size:11.5px;padding:6px 0;text-align:center;border:1px solid var(--lime-dark)}
.news-h{left:9px;top:672px;width:633px}
.sub{font-family:"Roboto Condensed",Arial,sans-serif;font-size:15px;color:#444}
.item{width:308px}
.item h3{font-size:9.6px;font-weight:700;color:#111;margin-bottom:5px;white-space:nowrap}
.item-row{display:flex;gap:8px}
.thumb{width:83px;height:57px;flex:none;background:linear-gradient(#c9d5e0,#7f94aa 45%,#1e2b44)}
.item p{font-size:9.4px;line-height:15px;color:#444;letter-spacing:.35px;padding-right:8px}
.item .more{text-align:right;font-size:11px;color:#333;margin-top:6px;padding-right:10px}
.col{width:166px}
.col .pic{height:93px;margin:6px 0 8px}
.col p{font-size:9.5px;line-height:15px;color:#555}
.col .btn-lime{width:73px;margin:9px 0 0 auto}
.links-h{left:662px;top:497px;width:159px}
.link-box{left:663px;width:158px;height:93px;border:1px solid #ddd;background:radial-gradient(#fff 55%,#eee);display:flex;align-items:center;justify-content:center;gap:5px;font-size:10.5px;font-weight:700;color:var(--blue-dark);text-align:center;padding:0 6px}
.link-box i{width:12px;height:12px;background:var(--blue);flex:none}
.footer{left:0;top:1163px;width:830px;height:37px;background:var(--footer);color:#999;font-size:10px;display:flex;align-items:center;padding:0 9px}
.social{display:flex;gap:5px}
.social i{width:20px;height:20px;background:#3d7cc9;border-radius:2px}
.foot-links{margin-left:246px}
.foot-copy{margin-left:auto}
</style>
</head>
<body>
<div class="abs topline"></div>

<header>
  <div class="abs brand">
    <div class="brand-mark"></div>
    <div class="brand-name">the shipping association of kelbury</div>
  </div>
  <div class="abs contact">
    <span><svg width="16" height="11" viewBox="0 0 16 11"><rect x=".5" y=".5" width="15" height="10" fill="none" stroke="#fff"/><path d="M1 1l7 5 7-5" fill="none" stroke="#fff"/></svg>info@kelbury.example</span>
    <span><svg width="12" height="12" viewBox="0 0 12 12"><path d="M2 1l2 0 1 3-1.5 1a7 7 0 0 0 3.5 3.5L8 7l3 1v2c0 1-1 1-2 1A9 9 0 0 1 1 3c0-1 0-2 1-2z" fill="#fff"/></svg>111-111-1234</span>
  </div>
  <nav class="abs nav">
    <a class="active">Home</a><a>Shipping Statistics</a><a>Case Studies</a><a>Career</a><a>Jobs</a><a>Contact</a>
  </nav>
</header>

<section class="abs hero" role="img" aria-label="Loaded container ship sailing near a port"></section>
<div class="abs dots"><i></i><i></i><i></i><i></i><i></i></div>

<form class="abs login">
  <div class="tabs"><span class="tab-on">Login</span><span class="tab-off">Register</span></div>
  <div class="login-body">
    <label>User ID :</label><div class="field"></div>
    <label>Password :</label><div class="field"></div>
    <div class="login-row"><span class="btn-blue">Login</span><span class="forgot">forgot password?</span></div>
  </div>
</form>

<h2 class="abs section welcome-h">Welcome to Shipping</h2>
<div class="abs photo welcome-img" role="img" aria-label="Port worker in a hard hat and safety vest at the docks"></div>
<p class="abs welcome-text">Founded in 1939 as a registered employers' trade union, the Shipping Association of Kelbury (KBU) represents 78 companies in the private sector of the island's shipping industry, and stands ready to forge additional alliances with key partners in the international industry. Membership includes shipping agents, wharf owners, terminal operators and stevedoring companies; together with ship owners and operators. The Shipping Association manages the supply of labour at Port Halloway. The KBU deals with all matters affecting the interest of its membership including industrial relations, security and training and</p>
<div class="abs btn-lime" style="left:569px;top:637px;width:73px">Read more</div>

<h2 class="abs section news-h">News</h2>
<div class="abs sub" style="left:9px;top:702px">Local</div>
<div class="abs sub" style="left:9px;top:834px">International</div>

<article class="abs item" style="left:9px;top:722px"><h3>Kelbury Opens Bid For Port Community System</h3><div class="item-row"><div class="photo thumb" role="img" aria-label="Container ship at a terminal"></div><p>The Port Authority of Kelbury (PAK) has launched the first of a two-stage tender process for the establishment of a Port Community System in Kelbury. ...</p></div><div class="more">Read more</div></article>
<article class="abs item" style="left:332px;top:722px"><h3>Kelbury Opens Bid For Port Community System</h3><div class="item-row"><div class="photo thumb" role="img" aria-label="Container ship at a terminal"></div><p>The Port Authority of Kelbury (PAK) has launched the first of a two-stage tender process for the establishment of a Port Community System in Kelbury. ...</p></div><div class="more">Read more</div></article>
<article class="abs item" style="left:9px;top:855px"><h3>Kelbury Opens Bid For Port Community System</h3><div class="item-row"><div class="photo thumb" role="img" aria-label="Container ship at a terminal"></div><p>The Port Authority of Kelbury (PAK) has launched the first of a two-stage tender process for the establishment of a Port Community System in Kelbury. ...</p></div><div class="more">Read more</div></article>
<article class="abs item" style="left:332px;top:855px"><h3>Kelbury Opens Bid For Port Community System</h3><div class="item-row"><div class="photo thumb" role="img" aria-label="Container ship at a terminal"></div><p>The Port Authority of Kelbury (PAK) has launched the first of a two-stage tender process for the establishment of a Port Community System in Kelbury. ...</p></div><div class="more">Read more</div></article>

<section class="abs col" style="left:9px;top:966px"><h2 class="section" style="border:0">Corporate video</h2><div class="photo pic" role="img" aria-label="Container ship at sea" style="background:linear-gradient(#d6e4f0,#8aa6c4 50%,#2a4468)"></div><p>Lorem Ipsum is simply dummy text of the printing and typesetting</p><div class="btn-lime">Read more</div></section>
<section class="abs col" style="left:242px;top:966px"><h2 class="section" style="border:0">Terminals</h2><div class="photo pic" role="img" aria-label="Ship under container cranes at a terminal" style="background:linear-gradient(#e4eef6,#9ab8d4 55%,#4a86b8)"></div><p>Lorem Ipsum is simply dummy text of the printing and typesetting</p><div class="btn-lime">Read more</div></section>
<section class="abs col" style="left:476px;top:966px"><h2 class="section" style="border:0">Careers</h2><div class="photo pic" role="img" aria-label="Business team in a meeting" style="background:linear-gradient(90deg,#d8d2c4,#b8a690 50%,#e8e6e2)"></div><p>Lorem Ipsum is simply dummy text of the printing and typesetting</p><div class="btn-lime">Read more</div></section>

<h2 class="abs section links-h">Links</h2>
<a class="abs link-box" style="top:530px"><i></i>Marrow Quay Limited</a>
<a class="abs link-box" style="top:632px"><i></i>TideCargo</a>
<a class="abs link-box" style="top:734px"><i></i>Ostrel Marine</a>
<a class="abs link-box" style="top:836px"><i></i>Dunmore Handlers Ltd</a>
<a class="abs link-box" style="top:938px"><i></i>Pellan Lines</a>
<a class="abs link-box" style="top:1040px"><i></i>Harbour Data Services Ltd.</a>

<footer class="abs footer">
  <div class="social" aria-label="Social links"><i></i><i></i><i></i></div>
  <div class="foot-links">Laws and regulation &nbsp;|&nbsp; Shipping terms</div>
  <div class="foot-copy">copyrigth © All Rights Reserved</div>
</footer>
</body>
</html>
```